CalmHarbor Homepage and Landing Pages

Please see detailed brief.

CalmHarbor is Australia’s newest online therapy and mental health service. We allow patients from across australia to connect with Mental health practitioners from across Australia. Our mission is to remove the friction in gaining support for mental health related issues.

Number of Pages Required

1 page

Font styles to use
Sans Serif

Colors
33a6d7
0293ce
3277b5
0255a3
acd136
9bcb3c

Requirements
Must have
• Please see detailed brief.
Nice to have
• Please see detailed brief
Should not have

```html
<!DOCTYPE html>
<html lang="en">
<head>
<meta charset="utf-8">
<title>CalmHarbor Homepage</title>
<link href="https://fonts.googleapis.com/css2?family=Roboto:wght@300;400;500;700&display=swap" rel="stylesheet">
<style>
:root{
  --stage:#6dcef5;
  --blue:#0857ce;
  --blue-deep:#0a55c9;
  --sky:#0aa5f2;
  --ink:#333;
  --muted:#777;
  --grey-bg:#f1f1f1;
  --white:#fff;
}
*{box-sizing:border-box;margin:0;padding:0}
html,body{width:1200px;height:1200px;overflow:hidden}
body{background:var(--stage);font-family:'Roboto',sans-serif;color:var(--ink);position:relative}
.abs{position:absolute}
.panel{position:absolute;top:0;width:566px;height:857px;background:var(--white);overflow:hidden}
.home{left:0}
.team-page{left:634px}
/* nav */
.nav{top:0;left:0;width:566px;height:37px;background:var(--white);font-size:5.5px;font-weight:500;color:#333}
.logo{display:flex;align-items:center;gap:4px;font-weight:400;color:#1a3a66}
.logo i{display:block;width:8px;height:8px;border-radius:50%;background:var(--sky)}
.nav .logo{left:30px;top:11px;font-size:12px}
.nav-link{top:15px}
.nav-link.active{color:var(--blue)}
.btn-sign{left:482px;top:10px;width:63px;height:16px;background:var(--blue);color:#fff;display:flex;align-items:center;justify-content:center}
/* hero */
.hero{top:37px;left:0;width:566px;height:265px;background:linear-gradient(90deg,#6b7276 0%,#8e9498 45%,#a7abad 100%)}
.hero-person{left:318px;top:28px;width:172px;height:240px;background:linear-gradient(180deg,#d9cfc6 0%,#f3f3f3 40%,#e8eaec 100%);border-radius:80px 80px 0 0}
.hero-copy{left:38px;top:50px;width:274px;text-align:center;color:#fff;z-index:1}
.hero-copy h1{font-size:23px;font-weight:500;letter-spacing:.2px}
.hero-copy p{font-size:7.6px;line-height:9px;margin-top:6px}
.btn-hero{display:inline-block;margin-top:10px;background:var(--blue);color:#fff;font-size:4.6px;font-weight:500;padding:5px 10px;border-radius:8px}
.dots{left:160px;top:242px;display:flex;gap:5px}
.dots span{width:5px;height:5px;border-radius:50%;background:rgba(255,255,255,.6)}
.dots span:first-child{background:#fff}
/* search */
.finder{left:29px;top:268px;width:507px;height:69px;background:var(--blue-deep)}
.finder h2{position:absolute;left:10px;top:8px;font-size:9.5px;font-weight:500;color:#fff}
.field{top:29px;height:28px;width:133px;background:#fff;font-size:7.4px;display:flex;align-items:center;justify-content:space-between;padding:0 9px 0 11px;color:#444}
.btn-search{top:29px;left:423px;width:75px;height:28px;background:var(--sky);color:#fff;font-size:7.6px;display:flex;align-items:center;justify-content:center;gap:4px}
/* mission */
.section-title{font-size:17.5px;font-weight:500;color:var(--blue);text-align:center}
.underline{height:2px;width:28px;background:var(--blue);margin:4px auto 0}
.mission{left:56px;top:405px;width:240px;text-align:center}
.mission p{font-size:10px;font-weight:300;color:var(--muted);line-height:12px;margin-top:10px}
.btn-block{display:inline-block;margin-top:16px;background:var(--blue);color:#fff;font-size:8.6px;font-weight:500;padding:8px 19px}
.phones{left:355px;top:372px;width:133px;height:198px;background:linear-gradient(160deg,#7fa35a 0%,#c9b8a4 45%,#e9e9e6 100%);border-radius:12px;border:3px solid #222}
.help{left:0;top:612px;width:566px;height:245px;background:var(--blue)}
.help-phone{left:88px;top:25px;width:98px;height:197px;background:linear-gradient(160deg,#6f9a50 0%,#cdbba6 50%,#ececea 100%);border-radius:12px;border:3px solid #222}
.help-copy{left:220px;top:55px;width:320px;text-align:center;color:#fff}
.help-copy h2{font-size:17.5px;font-weight:500}
.help-copy p{font-size:8.6px;line-height:10.4px;margin-top:9px}
.btn-sky{display:inline-block;margin-top:22px;background:var(--sky);color:#fff;font-size:8.6px;font-weight:500;padding:8px 13px}
/* team page */
.topbar{left:0;top:0;width:566px;height:21px;background:var(--blue)}
.team-head{left:30px;top:46px;width:506px;text-align:center}
.team-head p{font-size:8.5px;color:#444;line-height:10.5px;margin-top:10px}
.card{top:120px;width:165px;height:209px;background:#fff;border-radius:12px;box-shadow:0 1px 6px rgba(0,0,0,.18);text-align:center;overflow:hidden}
.avatar{width:65px;height:65px;border-radius:50%;background:var(--sky);margin:39px auto 0}
.card h3{font-size:10px;font-weight:400;margin-top:10px}
.card .addr{font-size:7.4px;color:#666;margin-top:1px}
.tag{display:inline-block;margin-top:13px;background:var(--blue);color:#fff;font-size:7.5px;padding:2px 11px;border-radius:8px}
.actions{position:absolute;left:0;bottom:0;width:100%;height:27px;border-top:1.5px solid #ddd;display:flex;font-size:4.6px;font-weight:500;color:#555}
.actions span{flex:1;display:flex;align-items:center;justify-content:center;gap:3px}
.actions span+span{border-left:1.5px solid #ddd}
.touch{left:0;top:352px;width:566px;height:318px;background:var(--grey-bg)}
.touch .section-title{position:absolute;left:0;top:22px;width:566px}
.contact-box{left:30px;top:65px;width:207px;height:219px;background:var(--sky);color:#fff;padding:20px 21px}
.contact-box h3{font-size:14.6px;font-weight:500}
.contact-row{display:flex;align-items:center;gap:17px;font-size:8.7px;margin-top:21px}
.contact-row:first-of-type{margin-top:20px}
.input{left:286px;width:208px;height:25px;background:#fff;font-size:7.5px;color:#444;padding:8px 11px}
.btn-send{left:286px;top:261px;width:88px;height:23px;background:var(--sky);color:#fff;font-size:8.6px;font-weight:500;display:flex;align-items:center;justify-content:center}
.news{left:0;top:670px;width:566px;height:46px;background:var(--blue)}
.news-input{left:30px;top:10px;width:198px;height:26px;background:#fff;font-size:7.4px;color:#444;display:flex;align-items:center;justify-content:space-between;padding:0 9px}
.social{top:18px;width:10px;height:10px;border-radius:50%;background:#fff}
.footer{left:0;top:717px;width:566px;height:116px;background:var(--blue);border-top:1px solid #3a7be0}
.footer .logo{left:30px;top:20px;font-size:16px;color:#1a3a70}
.col{top:27px;width:82px;color:#fff}
.col h4{font-size:7px;font-weight:500}
.col p{font-size:3.9px;line-height:4.6px;margin-top:8px}
.base{left:0;top:833px;width:566px;height:24px;background:var(--sky)}
.to-top{left:546px;top:814px;width:20px;height:20px;background:var(--sky);display:flex;align-items:center;justify-content:center}
</style>
</head>
<body>

<!-- Homepage -->
<section class="panel home">
  <header class="abs nav">
    <div class="abs logo"><i></i>CalmHarbor</div>
    <span class="abs nav-link active" style="left:136px">FOR PRACTITIONER</span>
    <span class="abs nav-link" style="left:209px">HOW IT WORKS</span>
    <span class="abs nav-link" style="left:272px">MEET OUR TEAM</span>
    <span class="abs nav-link" style="left:338px">CONTACT</span>
    <span class="abs nav-link" style="left:432px">&#9711; LOGIN</span>
    <span class="abs btn-sign">PATIENT SIGN IN</span>
  </header>

  <div class="abs hero" role="img" aria-label="Blurred clinic interior background">
    <div class="abs hero-person" role="img" aria-label="Smiling practitioner in a white coat with stethoscope"></div>
    <div class="abs hero-copy">
      <h1>WE'RE IN BETA!</h1>
      <p>CalmHarbor provides on-demand access to a range of psychologists &amp; personal<br>wellness professionals from across Australia.</p>
      <p style="margin-top:10px">Book your online appointment in minutes, 24/7.</p>
      <span class="btn-hero">FIND A PRACTITIONER</span>
    </div>
    <div class="abs dots"><span></span><span></span><span></span></div>
  </div>

  <div class="abs finder">
    <h2>I NEED TO FIND</h2>
    <div class="abs field" style="left:10px">DOCTOR
      <svg width="8" height="9" viewBox="0 0 8 9"><circle cx="4" cy="2.3" r="2.2" fill="#444"/><path d="M0 9c0-3 1.8-4.3 4-4.3S8 6 8 9z" fill="#444"/></svg></div>
    <div class="abs field" style="left:148px">SPECIALITY
      <svg width="9" height="10" viewBox="0 0 9 10" fill="none" stroke="#444" stroke-width=".8"><path d="M6 1v3a2 2 0 0 1-4 0V1"/><path d="M4 6v1.5a2 2 0 0 0 4 0V5"/><circle cx="8" cy="4.5" r=".8"/></svg></div>
    <div class="abs field" style="left:286px">LOCATION
      <svg width="7" height="9" viewBox="0 0 7 9"><path d="M3.5 0A3.4 3.4 0 0 0 0 3.4C0 6 3.5 9 3.5 9S7 6 7 3.4A3.4 3.4 0 0 0 3.5 0z" fill="#444"/><circle cx="3.5" cy="3.4" r="1.2" fill="#fff"/></svg></div>
    <div class="abs btn-search">
      <svg width="8" height="8" viewBox="0 0 8 8" fill="none" stroke="#fff" stroke-width="1.2"><circle cx="3.3" cy="3.3" r="2.5"/><path d="M5.2 5.2 7.5 7.5"/></svg>SEARCH</div>
  </div>

  <div class="abs mission">
    <h2 class="section-title">OUR MISSION IS SIMPLE</h2>
    <div class="underline"></div>
    <p>We want to break down the barriers in receiving<br>effective treatment and care for anxiety, stress and<br>mental health related issues.</p>
    <span class="btn-block">HOW IT WORKS?</span>
  </div>
  <div class="abs phones" role="img" aria-label="Two phones showing a smiling practitioner outdoors"></div>

  <div class="abs help">
    <div class="abs help-phone" role="img" aria-label="Phone showing a practitioner in a white coat"></div>
    <div class="abs help-copy">
      <h2>FIND THE HELP YOU NEED</h2>
      <p>Book an appointment with one of our highly qualified, licensed practitioners.<br>The consultation can be conducted from wherever you feel<br>most comfortable.</p>
      <p style="margin-top:10px">No travel. No Clinics.</p>
      <span class="btn-sky">FIND THE PRACTITIONER</span>
    </div>
  </div>
</section>

<!-- Team, contact and footer -->
<section class="panel team-page">
  <div class="abs topbar"></div>
  <div class="abs team-head">
    <h2 class="section-title">OUR TEAM</h2>
    <p>Our Practitioners are what makes CalmHarbor tick.&nbsp; However behind every great product is a hardworking team ensuring<br>that CalmHarbor can deliver the highest quality of service</p>
  </div>

  <article class="abs card" style="left:30px">
    <div class="avatar" role="img" aria-label="Practitioner portrait"></div>
    <h3>Dr. Ellis Marr</h3><p class="addr">48 Harbour Lane, Apt 12</p>
    <span class="tag">antropologi</span>
    <div class="actions"><span>&#9633; AVAILABILITY</span><span>&#9990; BOOK NOW</span></div>
  </article>
  <article class="abs card" style="left:201px">
    <div class="avatar" role="img" aria-label="Practitioner portrait"></div>
    <h3>Dr. Ellis Marr</h3><p class="addr">48 Harbour Lane, Apt 12</p>
    <span class="tag">antropologi</span>
    <div class="actions"><span>&#9633; AVAILABILITY</span><span>&#9990; BOOK NOW</span></div>
  </article>
  <article class="abs card" style="left:372px">
    <div class="avatar" role="img" aria-label="Practitioner portrait"></div>
    <h3>Dr. Ellis Marr</h3><p class="addr">48 Harbour Lane, Apt 12</p>
    <span class="tag">antropologi</span>
    <div class="actions"><span>&#9633; AVAILABILITY</span><span>&#9990; BOOK NOW</span></div>
  </article>

  <div class="abs touch">
    <div><h2 class="section-title">GET IN TOUCH</h2></div>
    <div class="abs underline" style="left:262px;top:44px;margin:0;width:40px"></div>
    <div class="abs contact-box">
      <h3>CONTACT US</h3>
      <div class="contact-row"><svg width="7" height="10" viewBox="0 0 7 9"><path d="M3.5 0A3.4 3.4 0 0 0 0 3.4C0 6 3.5 9 3.5 9S7 6 7 3.4A3.4 3.4 0 0 0 3.5 0z" fill="#fff"/><circle cx="3.5" cy="3.4" r="1.2" fill="#0aa5f2"/></svg>48 HARBOUR LANE, APT 12</div>
      <div class="contact-row"><svg width="9" height="7" viewBox="0 0 9 7"><rect width="9" height="7" fill="#fff"/><path d="M0 0l4.5 3.5L9 0" fill="none" stroke="#0aa5f2" stroke-width=".8"/></svg>HELLO@CALMHARBOR.EXAMPLE</div>
      <div class="contact-row"><svg width="9" height="9" viewBox="0 0 9 9"><path d="M2 0l2 2.3-1 1.2a6 6 0 0 0 2.5 2.5l1.2-1L9 7l-1.3 1.7C4.5 9 0 4.5.3 1.3z" fill="#fff"/></svg>02 5550 1234</div>
    </div>
    <div class="abs input" style="top:65px">YOUR NAME</div>
    <div class="abs input" style="top:103px">YOUR EMAIL</div>
    <div class="abs input" style="top:140px;height:105px">MESSAGE</div>
    <div class="abs btn-send">SEND</div>
  </div>

  <div class="abs news">
    <div class="abs news-input">ENTER YOUR EMAIL
      <svg width="11" height="8" viewBox="0 0 11 8" fill="none" stroke="#444" stroke-width=".9"><rect x=".5" y=".5" width="10" height="7"/><path d="M.5.5l5 4 5-4"/></svg></div>
    <span class="abs social" style="left:431px" aria-label="Social link"></span>
    <span class="abs social" style="left:463px" aria-label="Social link"></span>
    <span class="abs social" style="left:495px" aria-label="Social link"></span>
    <span class="abs social" style="left:526px" aria-label="Social link"></span>
  </div>

  <footer class="abs footer">
    <div class="abs logo"><i></i>CalmHarbor</div>
    <div class="abs col" style="left:185px"><h4>LATEST POST</h4>
      <p>Our team reviews every new practitioner to keep care safe and simple.</p>
      <p>Fresh tips on rest, stress and mood each week.</p></div>
    <div class="abs col" style="left:315px"><h4>HEAD OFFICE</h4>
      <p>Our team reviews every new practitioner to keep care safe and simple.</p>
      <p>Fresh tips on rest, stress and mood each week.</p></div>
    <div class="abs col" style="left:444px"><h4>QUICK LINES</h4>
      <p>Our team reviews every new practitioner to keep care safe and simple.</p>
      <p>Fresh tips on rest, stress and mood each week.</p></div>
  </footer>
  <div class="abs base"></div>
  <div class="abs to-top"><svg width="8" height="5" viewBox="0 0 8 5" fill="none" stroke="#fff" stroke-width="1.2"><path d="M.5 4.5 4 1l3.5 3.5"/></svg></div>
</section>

</body>
</html>
```